Book Cover Design for The Tinker's Ledger

We need a bold, attention-getting design for a book on a revolutionary new way of funding government spending - not only could we eliminate income taxes and finally balance the budget, but we could afford to pay everyone a basic income, provide free healthcare, free college, and a guaranteed retirement. See www.TheTinkersLedger.example to understand the proposition.

The book title is: The Tinker's Ledger

The subtitle is: When Every Ledger Finally Balances, Levies Vanish And Shares Arrive For Everyone

The author's name is: Brent Halvor

Target Market(s)

General population

Industry/Entity Type

Government

Font styles to use
Sans Serif

Requirements
Must have
• The blurb about the book, and about the author should be on the back cover, as should the author's photo.
• The book will be 5.5 x 8.5 inches and 165 pages long
Nice to have
• The subtitle should be prominent on the front cover, perhaps even above the title. The designer can use the sunrise photo as we do on the website to feature the subtitle, or not. We are open to all designs.

```html
<!DOCTYPE html>
<html lang="en">
<head>
<meta charset="utf-8">
<title>The Tinker's Ledger — Book Cover</title>
<link rel="stylesheet" href="https://fonts.googleapis.com/css2?family=Fira+Sans+Extra+Condensed:wght@600;700&family=Open+Sans:wght@300;700&family=PT+Sans:wght@400&display=swap">
<style>
  :root {
    --back-top: #7a5a1e;
    --back-mid: #6a3f12;
    --back-bottom: #4a2208;
    --spine: #4e3410;
    --front-glow: #fff8d8;
    --front-gold: #f2a21c;
    --front-orange: #e07a10;
    --front-deep: #b8500a;
    --headline-yellow: #f7c61a;
    --frame-orange: #e8961e;
    --ink-white: #ffffff;
    --ink-black: #111111;
  }
  * { margin: 0; padding: 0; box-sizing: border-box; }
  html, body { width: 1200px; height: 887px; overflow: hidden; background: #2b1606; }
  .cover { position: relative; width: 1200px; height: 887px; overflow: hidden; font-family: "PT Sans", sans-serif; color: var(--ink-white); }

  .back-cover {
    position: absolute; left: 0; top: 0; width: 574px; height: 887px;
    background:
      radial-gradient(ellipse 380px 260px at 560px 240px, rgba(190,140,50,0.35), transparent 70%),
      linear-gradient(180deg, var(--back-top) 0%, #76501a 30%, var(--back-mid) 60%, var(--back-bottom) 100%);
  }
  .back-title {
    position: absolute; left: 30px; top: 45px; width: 530px; text-align: center;
    font-family: "Fira Sans Extra Condensed", sans-serif; font-weight: 700;
    font-size: 31px; letter-spacing: 0.36em; padding-left: 0.36em; color: var(--headline-yellow); white-space: nowrap;
  }
  .blurb {
    position: absolute; left: 30px; top: 89px; width: 530px; text-align: center;
    font-size: 16px; line-height: 21px; white-space: nowrap;
  }
  .blurb p + p { margin-top: 11px; }

  .author-photo {
    position: absolute; left: 47px; top: 395px; width: 182px; height: 240px;
    border: 3px solid var(--frame-orange); border-radius: 2px;
    background: linear-gradient(160deg, #5d6a3a 0%, #8a7050 45%, #a2382c 80%, #2a2a2a 100%);
  }
  .author-bio {
    position: absolute; left: 253px; top: 389px; width: 300px;
    font-size: 16px; line-height: 21px; white-space: nowrap;
  }

  .spine {
    position: absolute; left: 574px; top: 0; width: 52px; height: 887px;
    background: linear-gradient(180deg, #5a3c12, var(--spine) 50%, #3e2208);
  }
  .spine-text {
    position: absolute; left: 0; width: 52px; writing-mode: vertical-rl;
    display: flex; align-items: center; justify-content: flex-start;
    font-family: "Fira Sans Extra Condensed", sans-serif; font-weight: 700;
    color: var(--ink-white); white-space: nowrap; line-height: 52px;
  }
  .spine-title { top: 50px; font-size: 27px; letter-spacing: 0.42em; }
  .spine-author { top: 663px; font-size: 30px; letter-spacing: 0.01em; }

  .front-cover {
    position: absolute; left: 626px; top: 0; width: 574px; height: 887px;
    background:
      radial-gradient(circle at 248px 200px, var(--front-glow) 0%, #ffe79a 9%, rgba(250,200,80,0.85) 20%, rgba(240,160,40,0) 48%),
      linear-gradient(180deg, #c88a1c 0%, var(--front-gold) 25%, var(--front-orange) 55%, var(--front-deep) 85%, #9a3e08 100%);
  }
  .front-text { position: absolute; left: 626px; top: 0; width: 574px; height: 887px; }
  .front-author {
    position: absolute; left: 0; top: 40px; width: 574px; text-align: center;
    font-family: "Fira Sans Extra Condensed", sans-serif; font-weight: 700;
    font-size: 72px; line-height: 1; color: var(--ink-black);
  }
  .front-subtitle {
    position: absolute; left: 10px; top: 496px; width: 554px; text-align: center;
    font-family: "Fira Sans Extra Condensed", sans-serif; font-weight: 600;
    font-size: 35px; line-height: 43px; color: var(--ink-white);
  }
  .front-title { position: absolute; left: 0; top: 678px; width: 574px; text-align: center; line-height: 1; font-family: "Open Sans", sans-serif; }
  .front-title .title-lead { display: block; font-weight: 700; font-size: 42px; }
  .front-title .title-main { display: block; font-weight: 700; font-size: 84px; letter-spacing: -0.03em; margin-top: -2px; }
  .front-title .title-tail { display: block; font-weight: 300; font-size: 60px; letter-spacing: 0.5em; padding-left: 0.5em; margin-top: -2px; }
</style>
</head>
<body>
<div class="cover">
  <section class="back-cover" role="img" aria-label="Warm sunset over a mountain ridge and pine forest, darkened for back cover text"></section>

  <h2 class="back-title">THE TINKER'S LEDGER</h2>
  <div class="blurb">
    <p>This is the story of how technology can transform our economy. If we<br>play it right, we can all win. When combined with a new understand-<br>ing of money, technology can eliminate the need for income taxes<br>while balancing the budget and paying off the national debt. We can<br>even afford a National Income, free higher education,<br>and free healthcare, while vastly reducing poverty.</p>
    <p>The solutions herein are nonpartisan, benefiting both rich and poor.<br>They could enable our nation to reach greater heights of prosperity<br>than we have ever achieved before. The answer is in restructuring<br>our financial system to stoke the production engine that technology<br>enables, instead of taxing prosperity as we do today.</p>
  </div>

  <div class="author-photo" role="img" aria-label="Portrait photo of author Brent Halvor outdoors"></div>
  <p class="author-bio">Halvor pioneered structured finance on<br>Harbor Row, architected the financing<br>for Tomas Verhoek's Redevelopment<br>Program, co-founded two nationally<br>acclaimed charter schools, co-founded<br>several successful technology<br>companies and launched a publication<br>for students read by millions in dozens<br>of countries. He has six children, lives<br>with his wife in Alder Ridge and<br>Palm Hollow, and enjoys solving national<br>economic problems.</p>

  <div class="spine">
    <div class="spine-text spine-title">THE TINKER'S LEDGER</div>
    <div class="spine-text spine-author">BRENT HALVOR</div>
  </div>

  <section class="front-cover" role="img" aria-label="Bright sunrise shining over a silhouetted pine forest in orange light"></section>
  <div class="front-text">
    <div class="front-author">BRENT HALVOR</div>
    <p class="front-subtitle">When Every Ledger Finally Balances,<br>Levies Vanish And Shares<br>Arrive For Everyone</p>
    <h1 class="front-title">
      <span class="title-lead">THE</span>
      <span class="title-main">TINKER'S</span>
      <span class="title-tail">LEDGER</span>
    </h1>
  </div>
</div>
</body>
</html>
```